Kolna Thai Massage Double Sided Flyer Luxury

I require a double sided flyer
we are a Thai Massage Spa
Would like gold, deep purple and bronze colours
Something eye catching and looks professional

```html
<!DOCTYPE html>
<html lang="en">
<head>
<meta charset="utf-8">
<title>Kolna Thai Massage – Double Sided Flyer</title>
<link rel="stylesheet" href="https://fonts.googleapis.com/css2?family=Montserrat:wght@700&family=Open+Sans:wght@400;600;700&display=swap">
<style>
  :root{
    --canvas:#f2f2f2;
    --plum:#692c4e;
    --gold:#fad044;
    --gold-text:#f9cf45;
    --white:#ffffff;
  }
  *{margin:0;padding:0;box-sizing:border-box;}
  html,body{width:1200px;height:1200px;overflow:hidden;background:var(--canvas);}
  .canvas{position:relative;width:1200px;height:1200px;background:var(--canvas);}

  .flyer{position:absolute;top:329px;width:388px;height:549px;background:var(--gold);overflow:hidden;}
  .flyer--front{left:197.5px;}
  .flyer--back{left:621px;}

  .block{position:absolute;left:0;width:388px;}
  .band-plum{background:var(--plum);}

  .photo-hero-front{top:7.5px;height:152px;background:linear-gradient(100deg,#f3b45a 0%,#f7d28b 35%,#e6a877 60%,#f2c896 100%);}
  .photo-hero-back{top:7.5px;height:152px;background:linear-gradient(90deg,#cfe4ee 0%,#e9d2c2 30%,#f1dccd 55%,#bcd9e4 80%,#d9a49a 100%);}
  .photo-room{top:298px;height:168.3px;background:linear-gradient(180deg,#8a6a55 0%,#c8b3a2 40%,#efe6dd 75%,#f7f3ee 100%);}
  .photo-strip{top:168.1px;height:87.5px;display:flex;}
  .photo-strip .tile{flex:1;height:100%;}
  .tile--face{background:linear-gradient(135deg,#f3ece6,#d9c3b4);}
  .tile--back{background:linear-gradient(135deg,#e8d4c6,#c99a84);}
  .tile--mask{background:linear-gradient(135deg,#eae4ea,#cdbfd0);}
  .tile--feet{background:linear-gradient(135deg,#f7f3ef,#e2cbbb);}

  .brand-panel{position:absolute;left:262px;top:0;width:126px;height:116px;}
  .brand-name{position:absolute;left:265px;width:114px;top:55px;text-align:center;
    font-family:"Open Sans",sans-serif;font-weight:400;font-size:7.5px;color:var(--gold-text);}
  .brand-mark-back{position:absolute;left:269px;top:50px;width:48px;height:48px;border:2px solid var(--plum);border-radius:50%;}
  .brand-name-back{position:absolute;left:223px;width:140px;top:104px;text-align:center;
    font-family:"Open Sans",sans-serif;font-weight:400;font-size:11px;color:var(--plum);}

  .line{position:absolute;left:0;right:0;text-align:center;transform:translateY(-50%);line-height:1.2;white-space:nowrap;}
  .heading{font-family:"Montserrat",sans-serif;font-weight:700;color:var(--gold-text);}
  .copy{font-family:"Open Sans",sans-serif;font-weight:400;color:var(--gold-text);font-size:6.6px;}
  .contact{font-family:"Open Sans",sans-serif;font-weight:700;color:var(--gold-text);font-size:6.8px;}
  .contact u{text-decoration:underline;}

  .welcome-copy{position:absolute;left:0;right:0;top:210px;text-align:center;
    font-family:"Open Sans",sans-serif;font-size:6.6px;line-height:9.6px;color:var(--gold-text);}

  .spa-badge{position:absolute;left:30.6px;top:420.6px;width:100px;height:100px;border-radius:50%;
    border:6px solid var(--gold);background:linear-gradient(135deg,#8d8279,#c2b3a8 50%,#d64f74 75%,#a69a8f);}

  .front-contact{position:absolute;right:21px;text-align:right;transform:translateY(-50%);
    font-family:"Open Sans",sans-serif;font-weight:700;font-size:6.8px;color:var(--gold-text);white-space:nowrap;}

  .divider{position:absolute;left:65px;width:259px;top:330px;height:0.6px;background:var(--gold);opacity:.8;}
</style>
</head>
<body>
<div class="canvas">

  <section class="flyer flyer--front">
    <div class="block photo-hero-front" role="img" aria-label="Woman relaxing face down during a back massage in warm golden light"></div>

    <svg class="brand-panel" viewBox="262 0 126 116" aria-hidden="true">
      <path d="M265 7.5 H379 V80 C350 80 315 112 265 108 Z" fill="var(--plum)"/>
      <path d="M265 7.5 V108 C315 112 350 80 388 80" fill="none" stroke="var(--gold)" stroke-width="4"/>
      <path d="M379 7.5 V80" fill="none" stroke="var(--gold)" stroke-width="4"/>
      <circle cx="322" cy="36" r="13" fill="none" stroke="var(--gold)" stroke-width="1.6"/>
    </svg>
    <div class="brand-name">Kolna Thai Massage</div>

    <div class="block band-plum" style="top:168.1px;height:121.3px;"></div>
    <div class="line heading" style="top:197.5px;font-size:16px;">Welcome to Luxury</div>
    <p class="welcome-copy">
      Set in the heart of Elmsworth, Kolna Thai Massage will allow you to immerse yourself in a place<br>
      where your wellbeing and rejuvenation is at the centre of what we do.<br>
      UsingThai traditions, our highly trained therapists offer revitalising<br>
      body treatments with their deep tissue massage techniques.<br>
      In their hands, you will see and feel immediate results.
    </p>

    <div class="block photo-room" role="img" aria-label="Two women resting on massage tables in a softly lit spa room"></div>

    <div class="block band-plum" style="top:475px;height:65.6px;"></div>
    <div class="spa-badge" role="img" aria-label="Rolled spa towels with pink orchid flowers and stones"></div>

    <div class="front-contact" style="top:489px;">Kolna Thai Massage | 42 Willow Row | Leeds | LS6 2QT</div>
    <div class="front-contact" style="top:498.5px;">0113 4960217 | <u>www.kolnathaimassage.co.uk</u></div>
    <div class="front-contact" style="top:517px;">Gift Vouchers Available</div>
  </section>

  <section class="flyer flyer--back">
    <div class="block photo-hero-back" role="img" aria-label="Smiling woman with a flower in her hair resting her head on her hands at a spa"></div>
    <div class="brand-mark-back" aria-hidden="true"></div>
    <div class="brand-name-back">Kolna Thai Massage</div>

    <div class="block photo-strip">
      <div class="tile tile--face" role="img" aria-label="Facial head massage"></div>
      <div class="tile tile--back" role="img" aria-label="Hands massaging a back"></div>
      <div class="tile tile--mask" role="img" aria-label="Facial mask treatment"></div>
      <div class="tile tile--feet" role="img" aria-label="Foot massage with rolled towel"></div>
    </div>

    <div class="block band-plum" style="top:264.4px;height:276.2px;"></div>

    <div class="line heading" style="top:285.5px;font-size:15px;">MASSAGES</div>
    <div class="line copy" style="top:303.5px;">Restore balance. Revive your senses. Discover all the ways Kolna Thai Massage</div>
    <div class="line copy" style="top:312.3px;">Can breathe new life into your body and soul.</div>
    <div class="divider"></div>

    <div class="line heading" style="top:351px;font-size:16px;">MASSAGES</div>
    <div class="line heading" style="top:367.3px;font-size:16px;">DEEP TISSUE MASSAGE</div>

    <div class="line heading" style="top:392.3px;font-size:12px;">60 minutes £45</div>
    <div class="line copy" style="top:404.8px;">Oil massage personalised, light to firm pressure</div>

    <div class="line heading" style="top:424.8px;font-size:12px;">90 minutes £55</div>
    <div class="line copy" style="top:437.4px;">Oil massage, medium to firm pressure</div>

    <div class="line heading" style="top:458.6px;font-size:11.5px;">THAI FLOOR TRADTIONAL MASSAGE</div>
    <div class="line heading" style="top:474.8px;font-size:12px;">60 minutes £45</div>
    <div class="line copy" style="top:487.4px;">Dry massage, medium to firm pressure applying stretching technique</div>

    <div class="line contact" style="top:506.5px;">Kolna Thai Massage | 42 Willow Row | Leeds | LS6 2QT | 0113 4960217 | <u>www.kolnathaimassage.co.uk</u></div>
    <div class="line contact" style="top:516.2px;">Gift Vouchers Available</div>
  </section>

</div>
</body>
</html>
```